Tinker's Fox sports bar beer & food menu

We need a menu design for our gastropub sports bar in L.A.'s Sawtelle Neighborhood (Little Osaka). We have a full-bar (hard liquor, craft beer, wine and cocktails) . We have a lunch and dinner menu as well as a happy hour menu. On Sundays we have a seperate menu with brunch items. The design concept is a British pub type of sports bar. We're looking for something different from our existing menu design. Ideally something cleaner and more legible. It should mesh a simple, modern sensibility with the more traditional darkened pub style of our interior design.

You can check out our Venuvista page for photos of the interior/exterior:
https://www.venuvista.com/biz_photos/tinkers-fox-los-angeles?tab=interior

You can view our existing menu here:
https://www.venuvista.com/biz_photos/tinkers-fox-los-angeles?tab=menu

If there's an area of the design that can be a little more playful it's our highlighted event schedule so that the events will stand out.

Target Market(s)

Age of 25 and up. Sawtelle is a cultural hub that caters to a younger, moderately affluent crowd.

Industry/Entity Type

Sports Bar

Font styles to use
Sans Serif

Colors

Designer to choose colors to be used in the design.

Requirements
Must have
• Logo, highlighted event schedule (beer pong Monday, trivia Tuesday, taco Tuesday, whiskey Wednesday, karaoke Saturday). The menu should be easy to read in a darkened bar. We'll be printing on standard 8.5x11 in portrait.
Nice to have
• We're trying to have the menu take up as few pages as possible.
Should not have
• We're trying to have the menu take up as few pages as possible. Food photography isn't necessary. A cover isn't necessary. Please avoid clip art of food.

```html
<!DOCTYPE html>
<html lang="en">
<head>
<meta charset="utf-8">
<title>Tinker's Fox — Menu</title>
<link href="https://fonts.googleapis.com/css2?family=Exo+2:ital,wght@0,400;0,600;0,700;1,400&display=swap" rel="stylesheet">
<style>
:root{
  --backdrop:#d0cece;
  --paper:#f3eedb;
  --frame:#dcc3ad;
  --ink:#1e1a16;
  --ink-soft:#3a342d;
  --accent:#f8ae3a;
  --rule:#5a5149;
}
*{box-sizing:border-box;margin:0;padding:0}
html,body{width:1200px;height:1015px;overflow:hidden;background:var(--backdrop)}
.stage{width:1300px;height:1100px;position:relative;transform:scale(.923077);transform-origin:0 0;font-family:"Exo 2",sans-serif;color:var(--ink)}
.page{position:absolute;width:601px;height:850px;background:var(--paper);box-shadow:4px 6px 10px rgba(0,0,0,.28)}
.page--left{left:34px;top:125px}
.page--right{left:660px;top:125px;width:605px;height:852px}
.frame{position:absolute;inset:12px;border:7px solid var(--frame);opacity:.85}
.brand{position:absolute;right:46px;top:42px;display:flex;align-items:center;gap:10px}
.brand__mark{width:30px;height:30px;border-radius:50%;background:var(--accent)}
.brand__text{display:flex;flex-direction:column;align-items:flex-start}
.brand__name{font-size:31px;font-weight:600;line-height:1;color:var(--ink)}
.brand__tag{font-size:7px;font-weight:400;letter-spacing:4px;margin-top:3px;color:var(--ink)}
.section{position:absolute;left:0;right:0}
.section__title{display:inline-block;margin-left:39px;width:195px;height:19px;background:var(--accent);font-size:12.5px;font-weight:700;line-height:19px;padding-left:6px;color:var(--ink-soft)}
.items{list-style:none;margin-top:9px;padding:0 48px 0 56px}
.item{position:relative;margin-bottom:9px}
.item__name{font-size:12px;font-weight:600;line-height:14px}
.item__price{position:absolute;right:0;top:0;font-size:12.5px;font-weight:700;line-height:14px}
.item__desc{font-size:7.4px;font-style:italic;line-height:9px;margin-left:8px;max-width:285px;color:var(--ink-soft)}
.items--plain .item{margin-bottom:4px}
.divider{position:absolute;height:0;border-top:1.5px dotted var(--rule)}
.events{position:absolute;height:16px;background:var(--accent);font-size:10.5px;font-weight:700;line-height:16px;text-align:center;color:var(--ink-soft);letter-spacing:.3px}
</style>
</head>
<body>
<div class="stage">

  <!-- Page one -->
  <section class="page page--left">
    <div class="frame" role="img" aria-label="Decorative patterned border"></div>
    <div class="brand">
      <span class="brand__mark"></span>
      <div class="brand__text"><span class="brand__name">Tinker's Fox</span><span class="brand__tag">PUB &amp; RESTAURANT</span></div>
    </div>

    <div class="section" style="top:118px">
      <h2 class="section__title">BURGERS AND SANDWICHES</h2>
      <ul class="items">
        <li class="item"><p class="item__name">Chicken Sandwich</p><span class="item__price">$12</span><p class="item__desc">Chicken Breast, Applewood Bacon, Butter Lettuce, White Cheddar, Avocado and Tomato Served on Sourdough Bread</p></li>
        <li class="item"><p class="item__name">Buttermilk Fried Chicken</p><span class="item__price">$13</span><p class="item__desc">Coleslaw, Provolone, Tomato, and a Spiced Mayonnaise on a Pretzel Roll</p></li>
        <li class="item"><p class="item__name">Short Rib Sandwich</p><span class="item__price">$13</span><p class="item__desc">Beef Shorts, Mayo, Tomato, Caramelized Onions, Arugula, Pepper Jack Cheese Served on Sourdough Bread</p></li>
        <li class="item"><p class="item__name">Grilled Cheese Sandwich</p><span class="item__price">$13</span><p class="item__desc">Cheese, Provolone and Cheddar Cheese</p></li>
        <li class="item"><p class="item__name">Tinker's Fox Burger</p><span class="item__price">$14</span><p class="item__desc">Sharp Cheddar, Arugula, Roasted Shallots, Bacon Jam with Malt Aioli</p></li>
        <li class="item"><p class="item__name">The Truffle Burger</p><span class="item__price">$15</span><p class="item__desc">Caramelized Onions, Arugula, Truffle Pecorino, Truffle Mayo and Truffle Fries</p></li>
        <li class="item"><p class="item__name">The Sloppy Joe</p><span class="item__price">$10</span><p class="item__desc">Shredded Lettuce and Sharp Cheddar</p></li>
        <li class="item"><p class="item__name">Veggie Burger</p><span class="item__price">$12</span><p class="item__desc">Concoction of Kale, Tomato, Avocado, Sharp Cheddar with a Balsamic Reduction</p></li>
        <li class="item"><p class="item__name">Flat Iron Steak Sandwich</p><span class="item__price">$16</span><p class="item__desc">Arugula, Peppers, Fontina, Onion and Mayo</p></li>
        <li class="item"><p class="item__name">Chicken Spinach Wrap</p><span class="item__price">$10</span><p class="item__desc">Chicken, Bacon, Lettuce, Tomato, Avocado, Ranch and Mayo</p></li>
        <li class="item"><p class="item__name">Fried Chicken Sliders (4)</p><span class="item__price">$12</span><p class="item__desc">Coleslaw, Lime Sriracha Sauce</p></li>
      </ul>
    </div>
    <div class="divider" style="top:515px;left:39px;width:254px"></div>
    <div class="divider" style="top:515px;left:323px;width:239px"></div>

    <div class="section" style="top:528px">
      <h2 class="section__title">BIG DOG BITES</h2>
      <ul class="items" style="margin-top:15px">
        <li class="item"><p class="item__name">Atlantic Cod Fish N' Chips</p><span class="item__price">$15</span><p class="item__desc">House Tartar Sauce, Vinegar and Lemon Wedge</p></li>
        <li class="item"><p class="item__name">Oven Roasted ½ Roasted Chicken</p><span class="item__price">$16</span><p class="item__desc">Boneless Chicken, Broccolini, Fingerling Potatoes, Topped with Chimichurri Sauce</p></li>
        <li class="item"><p class="item__name">Black Mussels</p><span class="item__price">$17</span><p class="item__desc">Tequila Chipotle Sauce, Cilantro and Cherry Tomatoes</p></li>
        <li class="item"><p class="item__name">Flat Iron Steak</p><span class="item__price">$19</span><p class="item__desc">French Fries, Baby Arugula in a Light peppercorn Sauce</p></li>
      </ul>
    </div>
    <div class="divider" style="top:692px;left:39px;width:254px"></div>
    <div class="divider" style="top:692px;left:323px;width:239px"></div>

    <div class="section" style="top:707px">
      <h2 class="section__title">FLATBREADS</h2>
      <ul class="items" style="margin-top:6px">
        <li class="item"><p class="item__name">Margherita</p><span class="item__price">$12</span><p class="item__desc">Fresh Mozzarella, Roma Tomatoes and Fresh Italian Basil</p></li>
        <li class="item"><p class="item__name">Vegetarian</p><span class="item__price">$13</span><p class="item__desc">Brussel Sprouts, Peppers, Onions, Zucchini, Goat Cheese, Smoked Mozzarella Topped with a Balsamic Reduction</p></li>
      </ul>
    </div>

    <p class="events" style="top:804px;left:39px;width:524px">•Beer Pong Monday •Trivia Tuesday •Taco Tuesday •Whiskey Wednesday •Karaoke Saturday</p>
  </section>

  <!-- Page two -->
  <section class="page page--right">
    <div class="frame" role="img" aria-label="Decorative patterned border"></div>
    <div class="brand">
      <span class="brand__mark"></span>
      <div class="brand__text"><span class="brand__name">Tinker's Fox</span><span class="brand__tag">PUB &amp; RESTAURANT</span></div>
    </div>

    <div class="section" style="top:106px">
      <ul class="items">
        <li class="item" style="margin-bottom:10px"><p class="item__name">Prosciutto &amp; Arugula</p><span class="item__price">$14</span><p class="item__desc">Red Onion, Parmesan, Mozzarella</p></li>
        <li class="item" style="margin-bottom:10px"><p class="item__name">Portobello &amp; Truffle</p><span class="item__price">$14</span><p class="item__desc">Portobello White Mushroom, Fontina, Drizzled with Truffle Oil</p></li>
        <li class="item" style="margin-bottom:10px"><p class="item__name">Chicken Tikka Masala</p><span class="item__price">$14</span><p class="item__desc">Tandoori Chicken, Fontini and Raita</p></li>
        <li class="item"><p class="item__name">The Tinker's Fox</p><span class="item__price">$15</span><p class="item__desc">Meatballs, Sausage, Chorizo, Mozzarella and Fresen</p></li>
      </ul>
    </div>
    <div class="divider" style="top:252px;left:40px;width:255px"></div>
    <div class="divider" style="top:252px;left:325px;width:240px"></div>

    <div class="section" style="top:271px">
      <h2 class="section__title" style="margin-left:40px">FOR THE TABLE</h2>
      <ul class="items" style="margin-top:6px">
        <li class="item"><p class="item__name">Tinker's 3 Whole Wings</p><span class="item__price">$9</span><p class="item__desc">Choice of Dry Rub, Sweet N' Spicy or Buffalo</p></li>
        <li class="item"><p class="item__name">Brussel Sprouts</p><span class="item__price">$8</span><p class="item__desc">Sautéed with Chorizo, Roasted Almonds and Golden Raisins</p></li>
        <li class="item"><p class="item__name">Golden Calamari</p><span class="item__price">$11</span><p class="item__desc">Traditionally Served with Spiced Marinara</p></li>
        <li class="item"><p class="item__name">Shrimp Mac N' Cheese</p><span class="item__price">$12</span><p class="item__desc">Baked with Fontina, Sharp Cheddar and Parmesan</p></li>
        <li class="item"><p class="item__name">S½ Dozen Oysters</p><span class="item__price">$12</span><p class="item__desc">Cedar Cove's Served with Our Own Mignonette</p></li>
        <li class="item"><p class="item__name">Charcuterie</p><span class="item__price">$15</span><p class="item__desc">Seasonal Meats and Cheese</p></li>
        <li class="item"><p class="item__name">Nachos</p><span class="item__price">$9</span><p class="item__desc" style="max-width:330px">Medley of Black Beans, Pico De Gallo, Cheese, Jalapeno and Sour Cream</p></li>
        <li class="item"><p class="item__name">Mozzarella Cheese Ctick</p><span class="item__price">$9</span></li>
      </ul>
    </div>
    <div class="divider" style="top:550px;left:40px;width:255px"></div>
    <div class="divider" style="top:550px;left:325px;width:240px"></div>

    <div class="section" style="top:568px">
      <h2 class="section__title" style="margin-left:40px">SIDES</h2>
      <ul class="items items--plain" style="margin-top:6px">
        <li class="item"><p class="item__name">House Fries</p><span class="item__price">$6</span></li>
        <li class="item"><p class="item__name">Truffle Fries</p><span class="item__price">$7</span></li>
        <li class="item"><p class="item__name">Dry Rub Fries</p><span class="item__price">$6</span></li>
        <li class="item"><p class="item__name">Sweet Potato Fries</p><span class="item__price">$7</span></li>
      </ul>
    </div>
    <div class="divider" style="top:676px;left:40px;width:255px"></div>
    <div class="divider" style="top:676px;left:325px;width:240px"></div>

    <div class="section" style="top:694px">
      <h2 class="section__title" style="margin-left:40px">DESSERT</h2>
      <ul class="items items--plain" style="margin-top:6px">
        <li class="item"><p class="item__name">Coco Flan</p><span class="item__price">$9</span></li>
        <li class="item"><p class="item__name">Cheese Cake</p><span class="item__price">$9</span></li>
        <li class="item"><p class="item__name">Peach Tart</p><span class="item__price">$9</span></li>
      </ul>
    </div>

    <p class="events" style="top:798px;left:46px;width:526px">•Beer Pong Monday •Trivia Tuesday •Taco Tuesday •Whiskey Wednesday •Karaoke Saturday</p>
  </section>

</div>
</body>
</html>
```